Tellbrook Mechanical Heating and Air Conditioning web page

This is a repair, installation and maintenance residential company. I don't do commercial. I need a web design that shows a company with 24/7 fast service that is easy for customers to contact me from. I am a Varnell /Oskiro HVAC dealer and their logos can be on there also. I also sell IAQ products like Zuvo- Crest and I offer duct cleanings as well.

Industry/Entity Type

Hvac

Coding

Coded - Design and coding required

Number of Pages Required

2 page

```html
<!DOCTYPE html>
<html lang="en">
<head>
<meta charset="utf-8">
<title>Tellbrook Mechanical Heating and Air Conditioning</title>
<link href="https://fonts.googleapis.com/css2?family=Fjalla+One&family=Open+Sans:wght@400;600&display=swap" rel="stylesheet">
<style>
:root{
  --blue:#1b8fe0;
  --blue-dark:#1572b8;
  --red:#e30613;
  --ink:#1e1e1e;
  --text:#444;
  --grey:#9a9a9a;
  --light:#eef0f2;
  --footer:#222;
  --white:#fff;
}
*{margin:0;padding:0;box-sizing:border-box}
html,body{width:1200px;height:3509px;overflow:hidden;background:var(--white)}
body{font-family:"Open Sans",sans-serif;color:var(--text)}
.page{position:relative;width:1200px;height:3509px;overflow:hidden}
.abs{position:absolute}
.display{font-family:"Fjalla One",sans-serif;font-weight:400}

/* header */
.site-header{position:absolute;left:0;top:0;width:1200px;height:111px;background:var(--white)}
.brand{left:144px;top:22px;color:var(--ink);font-family:"Fjalla One",sans-serif;line-height:1}
.brand .name{font-size:30px;letter-spacing:1px;display:block}
.brand .tag{font-size:11px;letter-spacing:2.4px;display:block;margin-top:6px}
.support{right:145px;top:18px;font-family:"Fjalla One",sans-serif;font-size:26px;color:var(--grey);display:flex;align-items:center;gap:8px}
.support .num{color:var(--red)}
.main-nav{right:145px;top:71px;display:flex;gap:38px;font-family:"Fjalla One",sans-serif;font-size:16px}
.main-nav a{color:var(--ink);text-decoration:none}
.main-nav a.active{color:var(--blue)}

/* hero */
.hero{left:0;top:111px;width:1200px;height:624px;background:linear-gradient(120deg,#b9b5b2 0%,#dedcda 40%,#eef0f3 70%,#d5dde5 100%)}
.hero-title{right:145px;top:130px;text-align:right;font-size:42px;line-height:50px;color:var(--ink)}
.btn{display:inline-block;font-family:"Fjalla One",sans-serif;font-size:17px;color:var(--white);text-align:center;border-radius:24px;text-decoration:none}
.btn-red{background:var(--red);right:145px;top:236px;width:127px;height:44px;line-height:44px}
.btn-blue{background:var(--blue);width:120px;height:44px;line-height:44px}
.btn-outline{border:2px solid var(--white);width:120px;height:42px;line-height:38px}
.hero-arrow{top:240px;width:48px;height:48px;border-radius:50%;background:#333;border:3px solid var(--white)}

/* welcome */
.welcome-title{left:145px;top:798px;font-size:42px;color:var(--blue)}
.welcome-text{left:145px;top:858px;width:510px;font-size:16.5px;line-height:33.5px;color:var(--text)}
.team-photo{left:694px;top:764px;width:360px;height:360px;border-radius:50%;background:linear-gradient(135deg,#dfe5ec,#2f4fa8 60%,#1c2f6e)}

/* services */
.services{left:0;top:1207px;width:1200px;height:620px;background:linear-gradient(160deg,#2a9aea 0%,#1b8fe0 50%,#1580d0 100%)}
.services-title{left:0;top:70px;width:1200px;text-align:center;font-size:40px;color:var(--white)}
.service{top:142px;width:300px;text-align:center;color:var(--white)}
.service .icon{width:208px;height:208px;border-radius:50%;background:var(--white);margin:0 auto;display:flex;align-items:center;justify-content:center}
.service h3{font-family:"Fjalla One",sans-serif;font-weight:400;font-size:34px;margin-top:14px;line-height:40px}
.service p{font-size:12px;line-height:21px;margin:12px 0 14px}

/* reviews */
.reviews-title{left:0;top:1945px;width:1200px;text-align:center;font-size:40px;color:var(--blue)}
.review-photo{left:144px;top:2032px;width:394px;height:394px;border-radius:50%;background:linear-gradient(160deg,#cdbf9f,#a99a7a 55%,#8b8b8b)}
.quote-text{left:630px;top:2128px;width:430px;font-size:20.5px;line-height:40px;color:var(--text)}
.quote-author{left:630px;top:2388px;font-size:22px;color:var(--blue-dark)}

/* contact */
.contact{left:0;top:2523px;width:1200px;height:500px;background:linear-gradient(100deg,#eceef0 0%,#f3f4f6 45%,#e9ecef 100%)}
.contact-photo{left:620px;top:40px;width:540px;height:460px;background:linear-gradient(135deg,#f2f3f5 0%,#e2e5e9 50%,#4c78ad 85%)}
.contact-title{left:145px;top:74px;font-size:42px;color:var(--blue)}
.field{position:absolute;height:44px;border:1.5px solid #c9ccd0;border-radius:22px;background:var(--white);font-size:12.5px;color:#888;padding-left:22px;line-height:41px}
.field.half{width:217px}
.field.full{width:441px}

/* brands */
.brands-title{left:0;top:3150px;width:1200px;text-align:center;font-size:40px;color:var(--blue)}
.brand-mark{top:3240px;height:66px;display:flex;align-items:center;justify-content:center;font-family:"Fjalla One",sans-serif;font-size:38px;color:#333}

/* footer */
.site-footer{left:0;top:3398px;width:1200px;height:111px;background:var(--footer);color:#aaa;font-size:11.5px}
.footer-links{left:144px;top:34px;display:flex;gap:10px}
.footer-links a{color:#aaa;text-decoration:none}
.copyright{left:144px;top:64px}
.social{top:29px;width:48px;height:48px;border-radius:50%;border:1.5px solid #888;display:flex;align-items:center;justify-content:center;font-size:10px;color:#aaa}
</style>
</head>
<body>
<div class="page">

  <header class="site-header">
    <div class="abs brand"><span class="name">TELLBROOK MECHANICAL</span><span class="tag">HEATING AND AIR CONDITIONING</span></div>
    <div class="abs support">24/7 SUPPORT
      <svg width="20" height="20" viewBox="0 0 24 24"><path fill="#e30613" d="M6.6 10.8a15 15 0 0 0 6.6 6.6l2.2-2.2a1 1 0 0 1 1-.25 11.4 11.4 0 0 0 3.6.57 1 1 0 0 1 1 1V20a1 1 0 0 1-1 1A17 17 0 0 1 3 4a1 1 0 0 1 1-1h3.5a1 1 0 0 1 1 1c0 1.25.2 2.45.57 3.6a1 1 0 0 1-.25 1z"/></svg>
      <span class="num">555 018 4427</span>
    </div>
    <nav class="abs main-nav">
      <a class="active" href="#">HOME</a><a href="#">SERVICES</a><a href="#">ABOUT US</a><a href="#">REVIEWS</a><a href="#">BLOG</a><a href="#">CONTACT US</a>
    </nav>
  </header>

  <section class="abs hero" role="img" aria-label="Wall-mounted air conditioning unit in a bright room">
    <h1 class="abs display hero-title">Phasellus condimentum<br>vitae faucibus cubilia</h1>
    <a class="abs btn btn-red" href="#">GET A QUOTE</a>
    <div class="abs hero-arrow" style="left:46px">
      <svg width="42" height="42" viewBox="0 0 42 42"><path d="M24 13l-8 8 8 8" fill="none" stroke="#fff" stroke-width="3.5"/></svg>
    </div>
    <div class="abs hero-arrow" style="left:1102px">
      <svg width="42" height="42" viewBox="0 0 42 42"><path d="M18 13l8 8-8 8" fill="none" stroke="#fff" stroke-width="3.5"/></svg>
    </div>
    <svg class="abs" style="left:0;top:479px" width="1200" height="146" viewBox="0 0 1200 146">
      <path d="M0 146 Q600 40 1200 18 L1200 146 Z" fill="#fff"/>
      <path d="M0 90 Q520 14 1200 10 L1200 18 Q600 40 0 146 Z" fill="#e30613"/>
    </svg>
  </section>

  <section class="welcome">
    <h2 class="abs display welcome-title">Welcome to Tellbrook Mechanical</h2>
    <p class="abs welcome-text">Phasellus nisl est, condimentum vitae faucibus in, sollicitudin vel metus. Nunc sit amet consequat risus. Curabitur ac elit leo eleifend dui tellus, in scelerisque elit porttitor et. Integer eu massa lacinia, lacinia nulla non, volutpat purus. Sed libero felis, vestibulum et dolor eget, lacinia aliquet neque.</p>
    <a class="abs btn btn-blue" style="left:145px;top:1042px" href="#">READ MORE</a>
    <div class="abs team-photo" role="img" aria-label="Two technicians in blue uniforms beside a service van"></div>
  </section>

  <section class="abs services" role="img" aria-label="Outdoor air conditioning units behind a blue overlay">
    <h2 class="abs display services-title">Services</h2>

    <div class="abs service" style="left:138px">
      <div class="icon">
        <svg width="110" height="110" viewBox="0 0 110 110" fill="none" stroke="#e30613" stroke-width="4" stroke-linecap="round">
          <path d="M22 20 L88 88"/><path d="M15 28 l10 -10 l8 8 l-10 10 z"/><path d="M80 80 l10 10"/>
          <path d="M88 22 L22 88"/><circle cx="90" cy="18" r="10"/><path d="M16 84 l10 10"/>
        </svg>
      </div>
      <h3>Repair</h3>
      <p>Integer eu massa lacinia, lacinia nulla non, volutpat purus. Sed libero felis, vestibulum et dolor eget, lacinia aliquet neque.</p>
      <a class="btn btn-outline" href="#">READ MORE</a>
    </div>

    <div class="abs service" style="left:450px">
      <div class="icon">
        <svg width="110" height="110" viewBox="0 0 110 110" fill="none" stroke="#e30613" stroke-width="4" stroke-linecap="round">
          <rect x="12" y="14" width="86" height="40" rx="6"/><path d="M24 40h62M24 47h62"/>
          <path d="M40 62 q4 6 0 12M52 62 q4 6 0 12M64 62 q4 6 0 12"/>
          <path d="M22 80v20M12 90h20M15 83l14 14M29 83l-14 14"/>
          <path d="M88 80v20M78 90h20M81 83l14 14M95 83l-14 14"/>
        </svg>
      </div>
      <h3>Installation</h3>
      <p>Integer eu massa lacinia, lacinia nulla non, volutpat purus. Sed libero felis, vestibulum et dolor eget, lacinia aliquet neque.</p>
      <a class="btn btn-outline" href="#">READ MORE</a>
    </div>

    <div class="abs service" style="left:763px">
      <div class="icon">
        <svg width="110" height="110" viewBox="0 0 110 110" fill="none" stroke="#e30613" stroke-width="4" stroke-linecap="round">
          <rect x="10" y="18" width="90" height="80"/><path d="M10 36h90"/>
          <path d="M52 12q6 6 0 12M62 12q6 6 0 12M72 12q6 6 0 12M82 12q6 6 0 12"/>
          <g fill="#e30613" stroke="none">
            <circle cx="26" cy="54" r="2.5"/><circle cx="40" cy="54" r="2.5"/><circle cx="54" cy="54" r="2.5"/><circle cx="68" cy="54" r="2.5"/><circle cx="82" cy="54" r="2.5"/>
            <circle cx="26" cy="68" r="2.5"/><circle cx="40" cy="68" r="2.5"/><circle cx="54" cy="68" r="2.5"/><circle cx="68" cy="68" r="2.5"/><circle cx="82" cy="68" r="2.5"/>
            <circle cx="26" cy="82" r="2.5"/><circle cx="40" cy="82" r="2.5"/><circle cx="54" cy="82" r="2.5"/><circle cx="68" cy="82" r="2.5"/><circle cx="82" cy="82" r="2.5"/>
          </g>
        </svg>
      </div>
      <h3>Maintenance</h3>
      <p>Integer eu massa lacinia, lacinia nulla non, volutpat purus. Sed libero felis, vestibulum et dolor eget, lacinia aliquet neque.</p>
      <a class="btn btn-outline" href="#">READ MORE</a>
    </div>
  </section>

  <svg class="abs" style="left:0;top:1810px" width="1200" height="140" viewBox="0 0 1200 140">
    <path d="M0 0 H1200 V24 Q700 4 0 17 Z" fill="#1580d0"/>
    <path d="M0 14 Q700 0 1200 24 L1200 138 Q980 40 0 18 Z" fill="#e30613"/>
  </svg>

  <section class="reviews">
    <h2 class="abs display reviews-title">Reviews</h2>
    <svg class="abs" style="left:52px;top:2210px" width="36" height="36" viewBox="0 0 36 36"><path d="M23 6L11 18l12 12" fill="none" stroke="#777" stroke-width="2.5"/></svg>
    <svg class="abs" style="left:1110px;top:2210px" width="36" height="36" viewBox="0 0 36 36"><path d="M13 6l12 12-12 12" fill="none" stroke="#777" stroke-width="2.5"/></svg>
    <div class="abs review-photo" role="img" aria-label="Customer relaxing in an armchair beneath a wall air conditioner"></div>
    <svg class="abs" style="left:629px;top:2030px" width="82" height="70" viewBox="0 0 82 70">
      <path fill="#c9c9c9" d="M0 70V36C0 14 10 2 34 0v14C22 16 18 22 18 32h16v38zM46 70V36C46 14 56 2 80 0v14C68 16 64 22 64 32h16v38z"/>
    </svg>
    <p class="abs quote-text">“ Proin placerat dapibus gravida. In tristique tristique nulla eget hendrerit. Maecenas vel tortor accumsan quam varius imperdiet vel eget elit. Aenean facilisis tincidunt lectus, id dictum nisi luctus eget. Vivamus efficitur ex condimentum, malesuada eros eget. ”</p>
    <p class="abs quote-author">- Dana Prewitt, City</p>
  </section>

  <section class="abs contact">
    <div class="abs contact-photo" role="img" aria-label="Technician servicing a wall-mounted air conditioner"></div>
    <h2 class="abs display contact-title">Contact us</h2>
    <div class="field half" style="left:145px;top:137px">Full Name</div>
    <div class="field half" style="left:369px;top:137px">Email</div>
    <div class="field half" style="left:145px;top:194px">Phone</div>
    <div class="field half" style="left:369px;top:194px">Service For
      <svg class="abs" style="right:18px;top:18px" width="12" height="8" viewBox="0 0 12 8"><path d="M0 0h12L6 8z" fill="#555"/></svg>
    </div>
    <div class="field half" style="left:145px;top:250px">Address Line 1</div>
    <div class="field half" style="left:369px;top:250px">Address Line 2</div>
    <div class="field full" style="left:145px;top:307px">Message</div>
    <a class="abs btn btn-blue" style="left:145px;top:370px" href="#">READ MORE</a>
  </section>

  <svg class="abs" style="left:0;top:2990px" width="1200" height="160" viewBox="0 0 1200 160">
    <path d="M0 0 H1200 V30 Q600 40 0 150 Z" fill="#eceef0"/>
    <path d="M0 110 Q520 30 1200 22 L1200 30 Q600 44 0 152 Z" fill="#e30613"/>
  </svg>

  <section class="brands">
    <h2 class="abs display brands-title">Brands we do service and Clean</h2>
    <div class="abs brand-mark" style="left:145px;width:262px">Varnell</div>
    <div class="abs brand-mark" style="left:447px;width:214px">Oskiro</div>
    <div class="abs brand-mark" style="left:720px;width:80px;font-size:28px">Zuvo</div>
    <div class="abs brand-mark" style="left:854px;width:202px;font-size:34px">Zuvo-Crest</div>
  </section>

  <footer class="abs site-footer">
    <nav class="abs footer-links">
      <a href="#">Home</a><span>|</span><a href="#">Services</a><span>|</span><a href="#">About Us</a><span>|</span><a href="#">Reviews</a><span>|</span><a href="#">Blog</a><span>|</span><a href="#">Contact Us</a>
    </nav>
    <p class="abs copyright">Copyright © 2020 &nbsp;Tellbrook Mechanical. &nbsp;All rights reserved.</p>
    <a class="abs social" style="left:942px" href="#" aria-label="Linkly">Linkly</a>
    <a class="abs social" style="left:1007px" href="#" aria-label="Snapra">Snapra</a>
  </footer>

</div>
</body>
</html>
```